IG ad to attract older men for better health #1

I want a bold headline Instagram Ad that coordinate with my website design with a racy sexy woman to attract men 45yrs old plus. See Two samples attached

Target Market(s)

Men 45 years old and older

Industry/Entity Type

Health And Wellness

Requirements
Must have
• eye catching appeal to men
Nice to have
• The copy to read
Kestrel61go is the headline at the top of the page. Then the copy reads...
"I want to seduce you to better health with a little T&A. Remove the excuses, provide ridiculously simple tips and advice to get you started on a path of lasting heath." Want more?

```html
<!DOCTYPE html>
<html lang="en">
<head>
<meta charset="UTF-8">
<title>Kestrel61go – Instagram Ad</title>
<link rel="stylesheet" href="https://fonts.googleapis.com/css2?family=Roboto+Condensed:wght@900&family=Montserrat:wght@600;700&display=swap">
<style>
  :root {
    --ink-black: #000000;
    --stage-glow: #3a3a3a;
    --brand-yellow: #ffd400;
    --copy-dark: #111111;
    --white: #ffffff;
    --tone-warm: #b98a70;
    --tone-deep: #5a3a2c;
  }
  html, body {
    margin: 0;
    padding: 0;
    width: 1200px;
    height: 1200px;
    overflow: hidden;
    background: var(--ink-black);
  }
  .ad {
    position: relative;
    width: 1200px;
    height: 1200px;
    overflow: hidden;
    background: radial-gradient(ellipse 620px 760px at 360px 120px, var(--stage-glow) 0%, #1a1a1a 45%, var(--ink-black) 80%);
  }
  .model-photo {
    position: absolute;
    left: 70px;
    top: 0;
    width: 450px;
    height: 1200px;
    background: radial-gradient(ellipse 260px 620px at 50% 50%, var(--tone-warm) 0%, var(--tone-deep) 60%, rgba(0,0,0,0) 100%);
  }
  .headline {
    position: absolute;
    top: 166px;
    left: 555px;
    width: 625px;
    margin: 0;
    text-align: center;
    font-family: "Roboto Condensed", sans-serif;
    font-weight: 900;
    font-size: 104px;
    line-height: 1;
    color: var(--brand-yellow);
    white-space: nowrap;
  }
  .quote-panel {
    position: absolute;
    left: 528px;
    top: 430px;
    width: 672px;
    height: 382px;
    background: var(--brand-yellow);
  }
  .quote-panel__text {
    position: absolute;
    left: 48px;
    right: 36px;
    top: 50px;
    margin: 0;
    text-align: center;
    font-family: "Montserrat", sans-serif;
    font-weight: 600;
    font-size: 31px;
    line-height: 45px;
    color: var(--copy-dark);
    white-space: nowrap;
  }
  .cta {
    position: absolute;
    left: 528px;
    width: 688px;
    top: 985px;
    margin: 0;
    text-align: center;
    font-family: "Montserrat", sans-serif;
    font-weight: 700;
    font-size: 52px;
    line-height: 1;
    color: var(--white);
  }
</style>
</head>
<body>
  <main class="ad">
    <div class="model-photo" role="img" aria-label="Photo of a long-haired brunette model in black lace lingerie standing against a dark studio backdrop"></div>
    <h1 class="headline">KESTREL61GO</h1>
    <section class="quote-panel">
      <p class="quote-panel__text">"I want to seduce you to better<br>health with a little T&amp;A.<br>Remove the excuses, provide<br>ridiculously simple tips and<br>advice to get you started on a<br>path of lasting heath."</p>
    </section>
    <p class="cta">WANT MORE ?</p>
  </main>
</body>
</html>
```